6x9 Postcard "401k Rollover" to market Individuals to transfer their retirement savings to our firm

Formats: .jpg, .png, .psd, .ai
Dimensions: See uploaded documents

We need a postcard to encourage people 45-65 years olds to transfer their retirement plan assets to our financial advising firm. We have uploaded an example we've been working please feel free to use your artistic license to make it look good images etc. You do not need to copy it word for word, we welcome creativity.

Suggested Wording:

We make it easy to rollover your old 401k

Spread the word! If you or someone you know has a 401k with a former employer or has reached age 59 1/2, consider a 401k rollover

The Pomfret Financial team can help rollover your old 401k

Advantages of a rollover: control over your accounts, more investment options, professional investment management, consolidate and simplify your accounts, guaranteed lifetime income options, help from a team of dedicated advisors

Make the most of your old 401k with a new Rollover IRA, speak with a trusted advisor today, (661)555-0147

If the QRM logo is used it MUST be used with the name "Gerald Pomfret" near it to clearly associate the two. if the words are used they Must be after his name and in all caps like this "Gerald Pomfret, ACCREDITED WEALTH STEWARD TM" [super script TM]. These are rules of the QRM trade mark.

Target Market(s)

Age 45 to 65 with sizable assets in 401k retirement plans

Industry/Entity Type

Investment Advisory

Font styles to use
Serif
Sans Serif
Decorative
Script

Colors

Designer to choose colors to be used in the design.

Requirements
Must have
• The post card MUST contain the following text at least 8pt font:
• Securities offered through Marlowe Ridge Securities, L.P. Member - NEVOA/DTRB | 4870 North Blvd K, Ste 210, Lancaster, CA 93536 | 800.555.0193 | CA Ins. Lic. #0K48391, #0519374, #0K27508, #0746290
• Must have website and phone number:
• www.geraldpomfretwealthco.com
• (661) 555-0147
Nice to have
• We would like the design to convey: Trust, Safety, Growth, Wealth, Planning, Strength, Stable, Peace of Mind, Time, Classic, Legacy

```html
<!DOCTYPE html>
<html lang="en">
<head>
<meta charset="utf-8">
<title>401k Rollover Postcard – Gerald Pomfret</title>
<link href="https://fonts.googleapis.com/css2?family=Lato:ital,wght@0,400;0,700;0,900;1,700&family=Libre+Baskerville:wght@700&display=swap" rel="stylesheet">
<style>
  :root{
    --bg:#2b2b2b;
    --gold:#f2a81d;
    --gold-light:#fcd25a;
    --ink:#231f20;
    --dark:#2e2d2e;
    --white:#ffffff;
    --grey:#d9d9d9;
    --grey-light:#f1f1f1;
    --line:#9a9a9a;
  }
  *{box-sizing:border-box;margin:0;padding:0}
  html,body{width:902px;height:1200px;overflow:hidden;background:var(--bg)}
  body{position:relative;font-family:"Lato",sans-serif;color:var(--ink)}
  .card{position:absolute;width:646px;height:432px;background:var(--white);overflow:hidden;box-shadow:0 8px 24px rgba(0,0,0,.45)}
  .abs{position:absolute}
  .gold-band{background:linear-gradient(90deg,var(--gold),var(--gold-light) 55%,var(--gold))}

  /* FRONT */
  .front{left:74px;top:100px}
  .photo{left:0;top:0;width:430px;height:250px;
    background:linear-gradient(120deg,#e9ecf1 0%,#c8cfdb 35%,#3a4a74 55%,#d8d1cb 75%,#f4f2ef 100%);
    clip-path:polygon(0 0,370px 0,430px 250px,0 250px)}
  .slash{left:372px;top:0;width:70px;height:250px;background:var(--gold);
    clip-path:polygon(0 0,8px 0,68px 250px,60px 250px)}
  .headline{left:380px;top:0;width:266px;height:250px;text-align:center;font-weight:900;text-transform:uppercase}
  .headline .small{position:absolute;left:0;width:266px;font-size:17px;font-weight:900;letter-spacing:.3px}
  .headline .band{position:absolute;right:0;height:54px;display:flex;align-items:center;justify-content:center}
  .kicker{top:40px}
  .rollover{top:70px;width:270px;font-size:46px;clip-path:polygon(0 0,100% 0,100% 100%,14px 100%)}
  .your-old{top:148px}
  .big-401k{top:178px;width:250px;height:58px;font-size:50px;clip-path:polygon(0 0,100% 0,100% 100%,14px 100%)}
  .disclaimer-band{left:0;top:250px;width:646px;height:58px;background:var(--dark)}
  .disclaimer{right:22px;top:262px;width:340px;color:var(--white);font-size:10px;font-weight:700;line-height:1.3;text-align:right}
  .name-block{left:0;top:280px;width:282px;height:116px;background:var(--white);
    clip-path:polygon(0 0,266px 0,282px 14px,282px 116px,0 116px)}
  .name{left:52px;top:306px;font-size:21px;font-weight:900;letter-spacing:.3px}
  .credential{display:flex;align-items:center;gap:8px}
  .credential .mark{width:18px;height:18px;background:var(--ink)}
  .credential .text{font-weight:900;color:var(--ink);line-height:1.15}
  .front .credential{left:54px;top:340px}
  .front .credential .text{font-size:11px;letter-spacing:1.8px}
  .call-row{left:322px;top:320px;display:flex;align-items:center}
  .phone-icon{width:40px;height:40px;border-radius:50%;background:var(--ink);border:3px solid var(--white);box-shadow:0 0 0 2px var(--ink);
    display:flex;align-items:center;justify-content:center;z-index:1}
  .call-pill{margin-left:-8px;height:28px;padding:0 16px 0 22px;border-radius:0 14px 14px 0;display:flex;align-items:center;gap:10px;font-size:19px}
  .call-pill .lead{color:var(--white);font-weight:700;font-size:15px}
  .call-pill .num{font-weight:700;color:var(--ink)}
  .web-row{left:290px;top:372px;font-size:10px;font-weight:700;line-height:16px;white-space:nowrap}
  .web-row .url{font-size:13px;margin-left:6px}
  .front-rule{left:0;top:398px;width:646px;height:3px;background:var(--ink)}
  .front-foot{left:0;top:404px;width:646px;height:28px}

  /* BACK */
  .back{left:195px;top:645px}
  .panel{left:0;top:0;width:370px;height:395px;background:var(--dark);clip-path:polygon(0 0,370px 0,310px 395px,0 395px)}
  .panel-stripe{left:300px;top:0;width:80px;height:395px;background:var(--gold);clip-path:polygon(70px 0,78px 0,18px 395px,10px 395px)}
  .spread{left:0;top:0;width:362px;height:52px;font-family:"Libre Baskerville",serif;font-size:14px;display:flex;align-items:center;justify-content:center;padding-right:30px;
    clip-path:polygon(0 0,100% 0,calc(100% - 8px) 100%,0 100%)}
  .intro{left:0;top:56px;width:352px;height:52px;background:linear-gradient(90deg,var(--grey),var(--white) 50%,var(--grey));
    font-size:10px;font-weight:700;text-transform:uppercase;text-align:center;line-height:1.25;padding:5px 20px 0 10px;
    clip-path:polygon(0 0,100% 0,calc(100% - 8px) 100%,0 100%)}
  .team{left:0;top:112px;width:344px;height:26px;background:linear-gradient(90deg,var(--grey-light),var(--white));font-size:9.5px;font-weight:700;
    display:flex;align-items:center;padding-left:28px;clip-path:polygon(0 0,100% 0,calc(100% - 6px) 100%,0 100%)}
  .adv-tag{left:0;top:146px;width:238px;height:20px;background:linear-gradient(90deg,var(--grey),var(--white));font-family:"Libre Baskerville",serif;font-size:11px;
    display:flex;align-items:center;padding-left:16px;clip-path:polygon(0 0,100% 0,calc(100% - 10px) 100%,0 100%)}
  .adv-list{left:16px;top:174px;list-style:none;color:var(--white);font-size:10.5px;font-weight:700;font-style:italic}
  .adv-list li{display:flex;align-items:center;gap:14px;height:18px}
  .adv-list svg{flex:none}
  .note{left:0;top:290px;width:336px;height:62px;background:linear-gradient(90deg,var(--grey-light),var(--white) 60%,var(--grey));
    font-size:7.4px;line-height:1.3;padding:7px 40px 0 16px;clip-path:polygon(0 0,100% 0,calc(100% - 8px) 100%,0 100%)}
  .note .sub{margin-top:5px;font-size:6.6px}
  .back-disclaimer{left:16px;top:358px;width:290px;color:var(--white);font-size:7.4px;line-height:1.25}
  .back-rule{left:0;top:398px;width:646px;height:2px;background:var(--ink)}
  .back-foot-left{left:0;top:402px;width:320px;height:30px;clip-path:polygon(0 0,100% 0,calc(100% - 12px) 100%,0 100%);
    display:flex;align-items:center;padding-left:22px;gap:8px;color:var(--white);font-size:13px;font-weight:700}
  .back-foot-left .num{font-size:19px;font-weight:700;color:var(--ink)}
  .back-foot-right{left:306px;top:402px;width:340px;height:30px;background:var(--dark);clip-path:polygon(14px 0,100% 0,100% 100%,0 100%);
    display:flex;align-items:center;padding-left:22px;color:var(--white);font-size:9px;font-weight:700}
  .back-foot-right .url{color:var(--gold-light);font-size:12px;margin-left:6px}
  .back-name{left:382px;top:22px;font-size:14px;font-weight:900;letter-spacing:.3px}
  .back .credential{left:384px;top:46px}
  .back .credential .mark{width:14px;height:14px}
  .back .credential .text{font-size:7.5px;letter-spacing:1.3px}
  .stamp{left:540px;top:18px;width:80px;height:84px;border:1px solid var(--ink)}
  .addr-line{left:386px;width:234px;height:1px;background:var(--line)}
</style>
</head>
<body>

<section class="card front">
  <div class="abs photo" role="img" aria-label="Photo of a smiling retired couple looking at a laptop together"></div>
  <div class="abs slash"></div>
  <div class="abs headline">
    <div class="small kicker">We make it easy to</div>
    <div class="band gold-band rollover">Rollover</div>
    <div class="small your-old">Your old</div>
    <div class="band gold-band big-401k">401K</div>
  </div>

  <div class="abs disclaimer-band"></div>
  <p class="abs disclaimer">Securities offered through Marlowe Ridge Securities, L.P. Member - NEVOA/DTRB | 4870 North Blvd K, Ste 210, Lancaster, CA 93536 | 800.555.0193 | CA Ins. Lic. #0K48391, #0519374, #0K27508, #0746290</p>

  <div class="abs name-block"></div>
  <h1 class="abs name">GERALD POMFRET</h1>
  <div class="abs credential">
    <span class="mark"></span>
    <span class="text">QRM ACCREDITED<br>WEALTH STEWARD™</span>
  </div>

  <div class="abs call-row">
    <span class="phone-icon">
      <svg width="18" height="18" viewBox="0 0 24 24"><path fill="#fff" d="M6.6 10.8a15.1 15.1 0 0 0 6.6 6.6l2.2-2.2c.3-.3.7-.4 1-.2 1.1.4 2.3.6 3.6.6.6 0 1 .4 1 1V20c0 .6-.4 1-1 1A17 17 0 0 1 3 4c0-.6.4-1 1-1h3.5c.6 0 1 .4 1 1 0 1.3.2 2.5.6 3.6.1.3 0 .7-.2 1z"/></svg>
    </span>
    <span class="call-pill gold-band"><span class="lead">Call us today!</span><span class="num">(661) 555-0147</span></span>
  </div>
  <p class="abs web-row">Visit us for more information : <span class="url">www.geraldpomfretwealthco.com</span></p>

  <div class="abs front-rule"></div>
  <div class="abs front-foot gold-band"></div>
</section>

<section class="card back">
  <div class="abs panel"></div>
  <div class="abs panel-stripe"></div>

  <h2 class="abs spread gold-band">SPREAD THE WORD!</h2>
  <p class="abs intro">If you or someone you know has a 401k with a former employer "or" has reached age 59 1/2; consider a 401k rollover</p>
  <p class="abs team">The Gerald Pomfret Financial Team can help rollover your old 401k</p>

  <h3 class="abs adv-tag">ADVANTAGES OF A ROLLOVER</h3>
  <ul class="abs adv-list">
    <li><svg width="10" height="9" viewBox="0 0 10 9"><path d="M1 5l3 3 5-7" fill="none" stroke="#fcd25a" stroke-width="2"/></svg>Control over your accounts</li>
    <li><svg width="10" height="9" viewBox="0 0 10 9"><path d="M1 5l3 3 5-7" fill="none" stroke="#fcd25a" stroke-width="2"/></svg>More investment options</li>
    <li><svg width="10" height="9" viewBox="0 0 10 9"><path d="M1 5l3 3 5-7" fill="none" stroke="#fcd25a" stroke-width="2"/></svg>Professional investment managment</li>
    <li><svg width="10" height="9" viewBox="0 0 10 9"><path d="M1 5l3 3 5-7" fill="none" stroke="#fcd25a" stroke-width="2"/></svg>Consolidate and simplify</li>
    <li><svg width="10" height="9" viewBox="0 0 10 9"><path d="M1 5l3 3 5-7" fill="none" stroke="#fcd25a" stroke-width="2"/></svg>Guaranteed lifetime income options</li>
    <li><svg width="10" height="9" viewBox="0 0 10 9"><path d="M1 5l3 3 5-7" fill="none" stroke="#fcd25a" stroke-width="2"/></svg>Help from a team of dedicated advisors</li>
  </ul>

  <div class="abs note">
    <p>Make the most of your old 401k with a new Rollover IRA through Marlowe Ridge Securities, 4870 North Blvd K Suite 210 Lancaster CA 93536 CA Ins. Lic. #0K48391 #0K27508 IRA, speak with a trusted advisor, 661-555-0147</p>
    <p class="sub">*Subject to employer plan rules</p>
  </div>
  <p class="abs back-disclaimer">Securities offered through Marlowe Ridge Securities, L.P. Member - NEVOA/DTRB | 4870 North Blvd K, Ste 210, Lancaster, CA 93536 | 800.555.0193 | CA Ins. Lic. #0K48391, #0519374, #0K27508, #0746290</p>

  <h2 class="abs back-name">GERALD POMFRET</h2>
  <div class="abs credential">
    <span class="mark"></span>
    <span class="text">QRM ACCREDITED<br>WEALTH STEWARD™</span>
  </div>
  <div class="abs stamp"></div>
  <div class="abs addr-line" style="top:210px"></div>
  <div class="abs addr-line" style="top:256px"></div>
  <div class="abs addr-line" style="top:302px"></div>

  <div class="abs back-rule"></div>
  <div class="abs back-foot-left gold-band">Call us today!
    <svg width="14" height="14" viewBox="0 0 24 24"><circle cx="12" cy="12" r="11" fill="none" stroke="#fff" stroke-width="2"/><path fill="#fff" d="M8.6 10.8a8 8 0 0 0 4.6 4.6l1.4-1.4c.2-.2.5-.3.7-.1l2 .6c.3.1.5.4.5.7V17c0 .4-.3.7-.7.7A10.5 10.5 0 0 1 6.3 6.9c0-.4.3-.7.7-.7h1.8c.3 0 .6.2.7.5l.6 2c.1.2 0 .5-.2.7z"/></svg>
    <span class="num">(661) 555-0147</span></div>
  <p class="abs back-foot-right">Visit us for more information : <span class="url">www.geraldpomfretwealthco.com</span></p>
</section>

</body>
</html>
```